Curtain and Blind Manufacturers - Retail Ecommerce All Pages

To Design a high converting website design for and improve on the domain www.velcourt-weaves.co.uk.

Generally it is improvements on what already exists, the core layout is functional and strong. Needs to have the header mobile responsive. Core elements for each page and clear content.

Current header is good just needs modernising and needs to work well on mobile. Need a way of having a mixture of categories and advice where necessary.

Pages and detailing required.
Home - Great Imagery for the sections. Category specific. A good product offering. So Call to product. Potentially straight to our best selling products. Not in a slider but in a straight forward grid. A nice simlar design to competitors in my space. shutterly4u, my own website. also i like websites like nessa mattresses, harrowdens.co.uk needs to be simple with clear direction for the customer particularly on mobile to get them to what we do quickly. EG curtains, blinds etc

Inner pages

Category Top Filters
https://www.velcourt-weaves.co.uk/flame-retardant/curtains

Category Side bar filters

Category Mobile with Off Canvas Filters

Product - Fabric
https://www.velcourt-weaves.co.uk/tovra-flame-retardant-curtain-fabric.html

Product - Curtains - https://www.velcourt-weaves.co.uk/tovra-fr-curtains.html

Product - Blinds
Cart
Checkout
Slide in Cart
Slide in Filters
General Content Page
About

```html
<!DOCTYPE html>
<html lang="en">
<head>
<meta charset="utf-8">
<title>Velcourt Weaves – Curtains, Blinds &amp; Fabrics</title>
<link href="https://fonts.googleapis.com/css2?family=Roboto:ital,wght@0,400;0,500;0,700;0,900;1,700&display=swap" rel="stylesheet">
<style>
:root{
  --red:#c8161d;
  --red-dark:#a50f15;
  --ink:#1a1a1a;
  --text:#333;
  --muted:#666;
  --line:#e2e2e2;
  --grey-bg:#e9e9e9;
  --footer:#1d1d1d;
  --white:#fff;
}
*{box-sizing:border-box;margin:0;padding:0}
html,body{width:1200px;height:4451px;overflow:hidden}
body{font-family:'Roboto',sans-serif;color:var(--text);background:var(--white);position:relative}
.abs{position:absolute}
.btn-red{position:absolute;background:var(--red);color:#fff;font-weight:700;font-size:12px;letter-spacing:.5px;display:flex;align-items:center;justify-content:center;border-radius:3px;text-transform:uppercase}

.topbar{position:absolute;top:0;left:0;width:1200px;height:22px;background:#111;color:#fff;font-size:9px;font-weight:500}
.topbar span{position:absolute;top:6px}
.header{position:absolute;top:22px;left:0;width:1200px;height:54px;border-bottom:1px solid var(--line)}
.search{position:absolute;left:112px;top:13px;width:263px;height:27px;border:1px solid #bbb;border-radius:2px;font-size:10px;color:#555;padding:7px 20px}
.search svg{position:absolute;right:12px;top:6px}
.logo{position:absolute;left:530px;top:10px;display:flex;align-items:center;gap:8px}
.logo i{display:block;width:32px;height:32px;background:var(--red);border-radius:3px}
.logo b{font-size:18px;font-weight:700;color:var(--red);letter-spacing:.3px;line-height:1;white-space:nowrap}
.h-item{position:absolute;top:15px;display:flex;align-items:center;gap:9px;font-size:10px;color:#333;white-space:nowrap}
.h-item svg{flex:none}
.nav{position:absolute;top:76px;left:112px;width:976px;height:32px;display:flex;justify-content:space-between;align-items:center;font-size:12px;font-weight:500;color:#222}

.hero{position:absolute;top:108px;left:0;width:1200px;height:585px;background:linear-gradient(120deg,#5b5751 0%,#8a7f72 35%,#b3a493 55%,#6d6660 80%,#3f3c39 100%)}
.hero h2{position:absolute;width:100%;text-align:center;top:163px;font-size:42px;font-weight:900;color:var(--red);letter-spacing:1px}
.hero h1{position:absolute;width:100%;text-align:center;top:215px;font-size:58px;font-weight:900;color:#fff;letter-spacing:1px}
.hero .dots{position:absolute;top:535px;left:563px;display:flex;gap:13px}
.hero .dots i{width:9px;height:9px;border-radius:50%;background:#fff;display:block}
.hero .dots i.on{background:var(--red)}

.partners{position:absolute;top:693px;left:0;width:1200px;height:107px;background:var(--grey-bg)}
.partner{position:absolute;top:37px;height:34px;background:#a8a8a8;border-radius:4px}

.sec-title{position:absolute;left:0;width:1200px;display:flex;justify-content:center;align-items:center;gap:22px;font-size:36px;font-weight:700;color:var(--ink)}
.sec-title::before,.sec-title::after{content:"";width:112px;height:1.5px;background:var(--red)}

.arrow{position:absolute;width:48px;height:48px;border-radius:50%;display:flex;align-items:center;justify-content:center}
.arrow.light{background:#fff;box-shadow:0 2px 8px rgba(0,0,0,.18)}
.arrow.dark{background:var(--red)}
.card{position:absolute;top:925px;width:237px;height:368px;background:#fff;box-shadow:0 1px 8px rgba(0,0,0,.12)}
.card .img{height:220px}
.card h3{margin-top:20px;text-align:center;font-size:11px;font-weight:500;color:#222;line-height:15px}
.card p{margin-top:12px;text-align:center;font-size:10px;color:#333}
.card .outline{position:absolute;left:56px;top:315px;width:126px;height:34px;border:1px solid var(--red);color:var(--red);border-radius:3px;font-size:10px;font-weight:700;display:flex;align-items:center;justify-content:center}

.promo{position:absolute;top:1447px;left:0;width:1200px;height:515px;background:var(--grey-bg)}
.promo-frame{position:absolute;left:17px;top:24px;width:1167px;height:470px;border:1px solid #c9c9c9}
.promo-vert{position:absolute;left:108px;transform:rotate(-90deg);transform-origin:left top;font-size:17px;font-weight:500;color:var(--red);letter-spacing:.5px;white-space:nowrap}
.promo .off{position:absolute;left:735px;top:143px;font-size:35px;font-weight:700;color:var(--red)}
.promo .brand{position:absolute;left:735px;top:202px;font-size:24px;font-weight:700;font-style:italic;color:#222}
.promo .coll{position:absolute;left:735px;top:240px;font-size:37px;font-weight:700;color:#111}

.cat{position:absolute;overflow:hidden;border-radius:2px}
.cat .label{position:absolute;left:0;bottom:0;width:100%;background:#1b1b1b;color:#fff;font-weight:700;font-size:18px;display:flex;align-items:center;justify-content:center;text-align:center;line-height:24px}

.features{position:absolute;top:2787px;left:0;width:1200px;height:232px;background:var(--red)}
.feat{position:absolute;top:38px;width:220px;text-align:center;color:#fff}
.feat .ic{width:86px;height:86px;border-radius:50%;background:#fff;margin:0 auto;display:flex;align-items:center;justify-content:center}
.feat h4{margin-top:20px;font-size:18px;font-weight:500}
.feat p{margin-top:8px;font-size:10px;line-height:14px}

.arrival{position:absolute;top:3159px;width:232px;text-align:center}
.arrival .img{height:266px}
.arrival h3{margin-top:22px;font-size:14px;font-weight:500;color:#222}
.arrival p{margin-top:12px;font-size:11px;color:#333}

.reviews{position:absolute;top:3553px;left:0;width:1200px;height:475px;background:var(--grey-bg)}
.review{position:absolute;top:147px;width:478px;height:251px;background:#fff;box-shadow:0 1px 6px rgba(0,0,0,.08)}
.review .avatar{position:absolute;left:40px;top:38px;width:86px;height:86px;border-radius:50%;border:2px solid var(--red);background:linear-gradient(160deg,#d8d2cc,#9f958c)}
.review h4{position:absolute;left:155px;top:58px;font-size:14px;font-weight:500;color:#111}
.review .role{position:absolute;left:155px;top:83px;font-size:10px;color:#444}
.review .stars{position:absolute;left:153px;top:98px;display:flex;gap:2px}
.review blockquote{position:absolute;left:62px;top:152px;width:380px;font-size:10px;line-height:18px;color:#444}
.review .q{position:absolute;font-size:34px;color:#ccc;font-weight:900;line-height:1}

.footer{position:absolute;top:4028px;left:0;width:1200px;height:423px;background:var(--footer);color:#fff}
.footer h5{font-size:13px;font-weight:700;letter-spacing:.3px;margin-bottom:10px}
.footer ul{list-style:none;font-size:9.5px;line-height:18.6px;color:#e8e8e8}
.f-col{position:absolute;top:63px}
.social li{display:flex;align-items:center;gap:12px;font-size:12px;height:42px}
.social li i{width:32px;height:32px;border-radius:50%;border:1.5px solid #fff;display:block}
.newsletter{position:absolute;left:840px;top:105px;width:248px;height:40px;border:1px solid #fff;border-radius:3px;display:flex}
.newsletter span{flex:1;font-size:9px;color:#ccc;padding:14px 18px}
.newsletter b{width:106px;background:#fff;color:#111;font-size:12px;display:flex;align-items:center;justify-content:center;border-radius:0 2px 2px 0}
</style>
</head>
<body>

<div class="topbar">
  <span style="left:112px">Up to 30% off + an extra 15% off lighting</span>
  <span style="right:112px">Free Delivery £250 Uk Ex S&amp;M</span>
</div>

<header class="header">
  <div class="search">Search
    <svg width="14" height="14" viewBox="0 0 14 14"><circle cx="6" cy="6" r="4.5" fill="none" stroke="#333" stroke-width="1.4"/><path d="M9.5 9.5l3.5 3.5" stroke="#333" stroke-width="1.4"/></svg>
  </div>
  <div class="logo"><i></i><b>VELCOURT WEAVES</b></div>
  <div class="h-item" style="left:773px">
    <svg width="26" height="26" viewBox="0 0 26 26"><circle cx="13" cy="13" r="12" fill="none" stroke="#333" stroke-width="1.3"/><path d="M9 7.5c-1 1-1 3 1 6s4.5 4.5 6 4.5c1 0 2-1 2-1.5l-2-2-1.5 1c-1 0-3.5-2.5-3.5-3.5l1-1.5-2-2z" fill="#333"/></svg>
    0161 4830297
  </div>
  <div class="h-item" style="left:912px">
    <svg width="26" height="26" viewBox="0 0 26 26"><circle cx="13" cy="13" r="12" fill="none" stroke="#333" stroke-width="1.3"/><circle cx="13" cy="10.5" r="3.5" fill="none" stroke="#333" stroke-width="1.3"/><path d="M6.5 20c1.5-3 4-4 6.5-4s5 1 6.5 4" fill="none" stroke="#333" stroke-width="1.3"/></svg>
    Account
  </div>
  <div class="h-item" style="left:1015px">
    <svg width="26" height="26" viewBox="0 0 26 26"><path d="M2 4h4l3 12h12l3-9H8" fill="none" stroke="#333" stroke-width="1.5"/><circle cx="11" cy="20.5" r="1.8" fill="#333"/><circle cx="19" cy="20.5" r="1.8" fill="#333"/></svg>
    Cart (0)
  </div>
</header>

<nav class="nav">
  <span>Home</span><span>About</span><span>Products</span><span>Curtains</span><span>Blinds</span><span>Furniture</span><span>Fabrics</span><span>Category</span><span>Contact</span><span>Blog</span>
</nav>

<section class="hero" role="img" aria-label="Modern bedroom with upholstered bed, slatted wall, floor lamp and large window with sheer curtains">
  <h2>WELCOME TO</h2>
  <h1>VELCOURT WEAVES</h1>
  <div class="btn-red" style="left:528px;top:307px;width:144px;height:43px">SHOP CURTAINS</div>
  <div class="dots"><i></i><i class="on"></i><i></i><i></i></div>
</section>

<section class="partners" aria-label="Trusted by">
  <div class="partner" style="left:210px;width:142px"></div>
  <div class="partner" style="left:452px;width:126px"></div>
  <div class="partner" style="left:692px;width:90px"></div>
  <div class="partner" style="left:888px;width:100px"></div>
</section>

<div class="sec-title" style="top:852px">Our Products</div>

<div class="arrow light" style="left:42px;top:1079px"><svg width="22" height="12" viewBox="0 0 22 12"><path d="M21 6H2M7 1L2 6l5 5" fill="none" stroke="#c8161d" stroke-width="1.5"/></svg></div>
<div class="arrow dark" style="left:1109px;top:1079px"><svg width="22" height="12" viewBox="0 0 22 12"><path d="M1 6h19M15 1l5 5-5 5" fill="none" stroke="#fff" stroke-width="1.5"/></svg></div>

<article class="card" style="left:112px">
  <div class="img" role="img" aria-label="Living room with leaf print curtains and fabric swatch" style="background:linear-gradient(135deg,#2f3a2c,#5c6b4d 50%,#8a7a63)"></div>
  <h3>Fernleaf Meadow Print<br>Flame Retardant Curtains</h3>
  <p>Excl. Tax: £54.17 &nbsp;&nbsp; Incl. Tax: £65.00</p>
  <div class="outline">VIEW PRODUCTS</div>
</article>
<article class="card" style="left:358px">
  <div class="img" role="img" aria-label="Grid of plain flame retardant curtain fabric swatches in many colours" style="background:linear-gradient(135deg,#d8c7a8,#b45a4a 45%,#6a2a3a 70%,#2f3556)"></div>
  <h3>VW Tovra Plain Flame Retardant<br>Curtains | Thermal</h3>
  <p>Excl. Tax: £54.17 &nbsp;&nbsp; Incl. Tax: £65.00</p>
  <div class="outline">VIEW PRODUCTS</div>
</article>
<article class="card" style="left:603px">
  <div class="img" role="img" aria-label="Swatches of textured curtain fabric in dark tones" style="background:linear-gradient(135deg,#3a3530,#5a4a3a 40%,#3a2a4a 70%,#22252c)"></div>
  <h3>Marlow Slub Weave FR<br>Curtains</h3>
  <p>Excl. Tax: £54.17 &nbsp;&nbsp; Incl. Tax: £65.00</p>
  <div class="outline">VIEW PRODUCTS</div>
</article>
<article class="card" style="left:849px">
  <div class="img" role="img" aria-label="Patterned floral and striped curtain fabrics with room setting" style="background:linear-gradient(135deg,#ecebe4,#cfd9c9 40%,#e2c9b7 70%,#b9a28f)"></div>
  <h3>Ashcombe Collection Flame<br>Retardant Curtains 25 Choices</h3>
  <p>Excl. Tax: £54.17 &nbsp;&nbsp; Incl. Tax: £65.00</p>
  <div class="outline">VIEW PRODUCTS</div>
</article>

<div class="btn-red" style="left:513px;top:1344px;width:175px;height:42px">VIEW ALL PRODUCTS</div>

<section class="promo">
  <div class="promo-frame"></div>
  <div class="promo-vert" style="top:292px">VELCOURT WEAVES</div>
  <div class="abs" role="img" aria-label="Folded teal and grey fabrics" style="left:149px;top:69px;width:180px;height:223px;border-radius:8px 0 0 0;background:linear-gradient(135deg,#4f8f95,#6a8f90 50%,#a7a59a)"></div>
  <div class="abs" role="img" aria-label="Stack of blue and white roller blind samples" style="left:242px;top:227px;width:178px;height:223px;background:linear-gradient(180deg,#1d5fd0,#2b6fe0 50%,#dfe6f2);border:3px solid #fff"></div>
  <div class="abs" role="img" aria-label="Bedroom with large window, neutral curtains and made bed" style="left:363px;top:69px;width:325px;height:336px;border:3px solid #fff;border-radius:0 0 70px 0;background:linear-gradient(160deg,#6b5a4a,#b7a58e 45%,#d9cdbd 60%,#4a3b30)"></div>
  <div class="off">30% OFF</div>
  <div class="brand">Velcourt-Weaves</div>
  <div class="coll">Modern Collections</div>
  <div class="btn-red" style="left:737px;top:320px;width:124px;height:41px">SHOP NOW</div>
</section>

<div class="sec-title" style="top:2013px">Categories</div>

<div class="cat" style="left:112px;top:2092px;width:479px;height:354px" role="img" aria-label="Hotel bedroom with dark bedding and curtains">
  <div style="height:100%;background:linear-gradient(160deg,#5d5d5f,#a9a9ab 40%,#3a3a44 75%,#1d1d24)"></div>
  <div class="label" style="height:60px">Flame Retardant Bedding</div>
</div>
<div class="cat" style="left:609px;top:2092px;width:478px;height:354px" role="img" aria-label="Close-up of white roller blind mechanism">
  <div style="height:100%;background:linear-gradient(150deg,#2f2f31,#6d6d70 35%,#e8e8e8 60%,#c9c9cc)"></div>
  <div class="label" style="height:60px">Fire Resistant Roller Blinds</div>
</div>
<div class="cat" style="left:114px;top:2467px;width:310px;height:247px" role="img" aria-label="Stage with purple theatre curtains">
  <div style="height:100%;background:linear-gradient(150deg,#2a1b4d,#6a3dbd 45%,#c9b6ea 65%,#352256)"></div>
  <div class="label" style="height:68px">Stage / Theatre Curtains</div>
</div>
<div class="cat" style="left:443px;top:2467px;width:309px;height:247px" role="img" aria-label="Light blue cubicle curtain on ceiling track">
  <div style="height:100%;background:linear-gradient(180deg,#e7eaee,#b7c9dd 50%,#8fb0d3)"></div>
  <div class="label" style="height:68px">Cubicle Curtains and<br>Tracks</div>
</div>
<div class="cat" style="left:771px;top:2467px;width:316px;height:247px" role="img" aria-label="Maroon vertical blind slats">
  <div style="height:100%;background:linear-gradient(90deg,#7a3445,#a75064 30%,#8a3c50 60%,#b35e70)"></div>
  <div class="label" style="height:68px">Vertical Blinds</div>
</div>

<section class="features">
  <div class="feat" style="left:77px">
    <div class="ic"><svg width="40" height="40" viewBox="0 0 40 40"><rect x="8" y="10" width="24" height="16" rx="2" fill="none" stroke="#c8161d" stroke-width="2"/><path d="M8 15h24" stroke="#c8161d" stroke-width="3"/><path d="M14 32h12M20 26v6" stroke="#c8161d" stroke-width="2"/></svg></div>
    <h4>Easy Payments</h4>
    <p>Low deposit, up to 4 years<br>to pay*</p>
  </div>
  <div class="feat" style="left:346px">
    <div class="ic"><svg width="42" height="40" viewBox="0 0 42 40"><path d="M4 12h22v16H4zM26 17h7l5 6v5H26z" fill="#c8161d"/><circle cx="11" cy="30" r="3.5" fill="#c8161d" stroke="#fff" stroke-width="1.5"/><circle cx="32" cy="30" r="3.5" fill="#c8161d" stroke="#fff" stroke-width="1.5"/></svg></div>
    <h4>In home premier delivery</h4>
    <p>Best in class</p>
  </div>
  <div class="feat" style="left:646px">
    <div class="ic"><svg width="40" height="40" viewBox="0 0 40 40"><circle cx="20" cy="16" r="10" fill="none" stroke="#c8161d" stroke-width="2.4"/><path d="M15 16l4 4 6-7" fill="none" stroke="#c8161d" stroke-width="2.4"/><path d="M13 24l-3 12 5-3 3 4 2-9M27 24l3 12-5-3-3 4-2-9" fill="#c8161d"/></svg></div>
    <h4>Buy with confidence</h4>
    <p>Store established in 1899</p>
  </div>
  <div class="feat" style="left:903px">
    <div class="ic"><svg width="40" height="40" viewBox="0 0 40 40"><circle cx="12" cy="11" r="3" fill="#c8161d"/><circle cx="20" cy="9" r="3" fill="#c8161d"/><circle cx="28" cy="11" r="3" fill="#c8161d"/><path d="M6 28c4-4 8-5 12-3l6 1c2 0 2 3 0 3h-6M6 32l10 3 16-8c2-1 1-4-2-3l-8 3" fill="none" stroke="#c8161d" stroke-width="2.2"/></svg></div>
    <h4>Rated Excellent</h4>
    <p>Read our Reviews</p>
  </div>
</section>

<div class="sec-title" style="top:3080px">New Arrivals</div>

<article class="arrival" style="left:112px">
  <div class="img" role="img" aria-label="Stack of white flame retardant pillows" style="background:linear-gradient(160deg,#f5f5f5,#dcdcdc 50%,#f2f2f2)"></div>
  <h3>Flame Retardant Pillow</h3>
  <p>Excl. Tax: £10.42 Incl. Tax: £12.50</p>
</article>
<article class="arrival" style="left:360px">
  <div class="img" role="img" aria-label="Grey roman blind over a window in a kitchen" style="background:linear-gradient(180deg,#5e5954,#6f6a64 40%,#c8c6bd 60%,#e9e6e0)"></div>
  <h3>Flame Retardant Roman Blinds</h3>
  <p>Excl. Tax: £183.33 Incl. Tax: £220.00</p>
</article>
<article class="arrival" style="left:607px">
  <div class="img" role="img" aria-label="White cord operated curtain track with gliders" style="background:linear-gradient(160deg,#f7f7f7,#e3e3e3 50%,#f3f3f3)"></div>
  <h3>Stage Cord Operated Track</h3>
  <p>Excl. Tax: £66.67 Incl. Tax: £80.00</p>
</article>
<article class="arrival" style="left:854px">
  <div class="img" role="img" aria-label="Dark green flame retardant curtains" style="background:linear-gradient(90deg,#15221a,#2b3b2f 30%,#18251c 60%,#2f4133)"></div>
  <h3>Flame Retardant Curtains</h3>
  <p>Excl. Tax: £99.99 Incl. Tax: £119.99</p>
</article>

<section class="reviews">
  <div class="sec-title" style="top:57px">What Our Customers Say</div>
  <div class="arrow light" style="left:42px;top:240px"><svg width="22" height="12" viewBox="0 0 22 12"><path d="M21 6H2M7 1L2 6l5 5" fill="none" stroke="#c8161d" stroke-width="1.5"/></svg></div>
  <div class="arrow dark" style="left:1109px;top:240px"><svg width="22" height="12" viewBox="0 0 22 12"><path d="M1 6h19M15 1l5 5-5 5" fill="none" stroke="#fff" stroke-width="1.5"/></svg></div>

  <article class="review" style="left:112px">
    <div class="avatar" role="img" aria-label="Customer portrait"></div>
    <h4>Marcel Dunford</h4>
    <div class="role">Designer</div>
    <div class="stars"><svg width="94" height="18" viewBox="0 0 94 18"><g fill="#f5b800"><path id="s1" d="M9 1l2.4 5 5.4.6-4 3.7 1.1 5.4L9 13 4.1 15.7l1.1-5.4-4-3.7 5.4-.6z"/><use href="#s1" x="19"/><use href="#s1" x="38"/><use href="#s1" x="57"/><use href="#s1" x="76"/></g></svg></div>
    <span class="q" style="left:32px;top:150px">“</span>
    <blockquote>Lorem ipsum dolor sit amet, consectetur adipiscing elit, sed do eiusmod tempor incididunt ut labore et dolore magna aliqua. Quis ipsum suspendisse ultrices gravida. Risus commodo viverra maecenas accumsan lacus vel facilisis.</blockquote>
    <span class="q" style="left:132px;top:208px">”</span>
  </article>
  <article class="review" style="left:609px">
    <div class="avatar" role="img" aria-label="Customer portrait"></div>
    <h4>Priya Ellwood</h4>
    <div class="role">Business consultant</div>
    <div class="stars"><svg width="94" height="18" viewBox="0 0 94 18"><g fill="#f5b800"><path id="s2" d="M9 1l2.4 5 5.4.6-4 3.7 1.1 5.4L9 13 4.1 15.7l1.1-5.4-4-3.7 5.4-.6z"/><use href="#s2" x="19"/><use href="#s2" x="38"/><use href="#s2" x="57"/><use href="#s2" x="76"/></g></svg></div>
    <span class="q" style="left:32px;top:150px">“</span>
    <blockquote>Lorem ipsum dolor sit amet, consectetur adipiscing elit, sed do eiusmod tempor incididunt ut labore et dolore magna aliqua. Quis ipsum suspendisse ultrices gravida. Risus commodo viverra maecenas accumsan lacus vel facilisis.</blockquote>
    <span class="q" style="left:98px;top:208px">”</span>
  </article>
</section>

<footer class="footer">
  <div class="abs" style="left:112px;top:60px;display:flex;align-items:center;gap:10px">
    <i style="display:block;width:36px;height:36px;background:#fff;border-radius:3px"></i>
    <b style="font-size:20px;font-weight:700;color:#fff;line-height:1.05">VELCOURT<br>WEAVES</b>
  </div>
  <p class="abs" style="left:112px;top:123px;font-size:9px;line-height:14px;color:#ddd">© Velcourt Weaves 2023.All rights<br>reserved</p>

  <div class="f-col" style="left:308px">
    <h5>USEFUL LINKS</h5>
    <ul>
      <li>About Us</li><li>FAQ - Frequently Asked Questions</li><li>Curtain and Blind Installation</li><li>Nationwide</li><li>How to Measure for Curtains and</li><li>Blinds</li><li>Terms and Conditions</li><li>Privacy Policy</li><li>Blog</li><li>Delivery &amp; Shipping Information</li><li>Returns &amp; Cancellation</li><li>Client Reviews</li><li>Contact Us</li><li>Charity</li>
    </ul>
  </div>

  <div class="f-col" style="left:494px">
    <h5>OUR PRODUCTS</h5>
    <ul>
      <li>Flame Retardant Curtains</li><li>Fire Resistant Blinds</li><li>Made to Measure Curtains</li><li>Acoustic Curtains</li><li>Curtain Fabrics</li><li>Curtain Poles</li><li>Curtain Tracks</li>
    </ul>
    <h5 style="margin-top:24px">GET IN CONTACT</h5>
    <ul style="line-height:19px">
      <li>T : 0161 483 0297</li><li>Mon - Fri 9am - 5pm</li><li>Harlow Textile Holdings LTD</li><li>Velcourt Weaves</li><li style="line-height:11px;padding-top:4px">Unit 7, Larkfield Mill<br>Road</li><li>Bristol, BS12 4PQ</li>
    </ul>
  </div>

  <ul class="f-col social" style="left:680px;top:56px">
    <li><i></i>Facepage</li><li><i></i>Chirper</li><li><i></i>Snapgram</li><li><i></i>Pinboard</li><li><i></i>Workednet</li><li><i></i>Searchly</li><li><i></i>Viewtube</li>
  </ul>

  <div class="f-col" style="left:840px">
    <h5>SUBSCRIBE TO OUR NEWSLETTER</h5>
  </div>
  <div class="newsletter"><span>Enter your email</span><b>Subscribe</b></div>
</footer>

</body>
</html>
```